Business Card Design

Quorvel Software Limited develops and sells venue and event management software called Quorvel Stagehand, which is available in the cloud or on-premise. The company was established in 1986. Most of our customers are performing arts venues, museums and festivals. Our existing design is a bit dull. We need to convey that we are both innovative and reliable.
Not all our people show their mobile phone numbers on their cards, so the design needs to work land line and mobile or land line only.

Industry/Entity Type

Software

Contact Information for Business Card

Helen Trasko
Director
Quorvel Software Limited
42B Milbrook Lane, Epsom, Surrey, KT19 4DN
Telephone: +44 (0)1372 640913
Mobile: +44 (0)7945 216804
Email: htrasko@quorvel.net
Web: www.quorvel.net

```html
<!DOCTYPE html>
<html lang="en">
<head>
<meta charset="utf-8">
<title>Quorvel Software Limited – Business Card</title>
<link rel="stylesheet" href="https://fonts.googleapis.com/css2?family=Lato:wght@400;700;900&display=swap">
<style>
  :root {
    --backdrop: #3a3b3d;
    --card-black: #020203;
    --card-white: #ffffff;
    --brand-blue: #0f4d78;
    --brand-blue-bright: #1d5f8f;
    --ink: #123a5a;
    --band-text: #e8eef3;
  }
  * { box-sizing: border-box; margin: 0; padding: 0; }
  html, body { width: 1200px; height: 926px; overflow: hidden; }
  body {
    background: var(--backdrop);
    font-family: "Lato", Arial, sans-serif;
    display: flex;
    flex-direction: column;
    align-items: center;
    justify-content: center;
    gap: 52px;
  }
  .card {
    position: relative;
    width: 640px;
    height: 380px;
    overflow: hidden;
    box-shadow: 0 10px 28px rgba(0,0,0,0.45);
  }

  /* Brand lockup */
  .brand {
    display: flex;
    align-items: center;
    gap: 16px;
    color: var(--brand-blue-bright);
    font-weight: 900;
    letter-spacing: 2px;
  }
  .brand-mark {
    width: 44px;
    height: 44px;
    background: var(--brand-blue-bright);
  }

  /* Front side */
  .card-front { background: var(--card-black); }
  .card-front .brand {
    position: absolute;
    left: 50%;
    top: 140px;
    transform: translateX(-50%);
    font-size: 46px;
  }
  .web-band {
    position: absolute;
    left: 0; right: 0; bottom: 0;
    height: 40px;
    background: var(--brand-blue);
    color: var(--band-text);
    font-size: 15px;
    letter-spacing: 11px;
    display: flex;
    align-items: center;
    justify-content: center;
  }

  /* Back side */
  .card-back { background: var(--card-white); }
  .back-header {
    height: 158px;
    background: var(--card-black);
    display: flex;
    align-items: center;
    justify-content: center;
  }
  .card-back .brand { font-size: 40px; padding-top: 24px; }
  .card-back .brand-mark { width: 38px; height: 38px; }

  .holder {
    position: absolute;
    top: 176px;
    left: 0; right: 0;
    text-align: center;
    color: var(--ink);
    font-size: 25px;
    font-weight: 400;
  }
  .holder strong { font-weight: 700; }
  .holder .role { margin-left: 6px; }

  .company-block {
    position: absolute;
    left: 30px;
    top: 222px;
    color: var(--ink);
  }
  .company-name { font-size: 18px; font-weight: 700; margin-bottom: 4px; }
  .company-address { font-size: 14px; line-height: 1.35; }

  .contact-list {
    position: absolute;
    right: 30px;
    top: 266px;
    color: var(--ink);
    font-size: 16px;
    line-height: 1.28;
    display: grid;
    grid-template-columns: 28px auto;
    column-gap: 8px;
  }
  .contact-list dt { font-weight: 900; }

  .foot-stripe {
    position: absolute;
    left: 0; right: 0; bottom: 0;
    height: 14px;
    background: var(--brand-blue);
    border-top: 4px solid var(--card-white);
    box-shadow: 0 -2px 0 var(--brand-blue);
  }
</style>
</head>
<body>

  <section class="card card-front" aria-label="Card front">
    <div class="brand"><span class="brand-mark"></span><span class="brand-name">QUORVEL</span></div>
    <div class="web-band">www.quorvel.net</div>
  </section>

  <section class="card card-back" aria-label="Card back">
    <header class="back-header">
      <div class="brand"><span class="brand-mark"></span><span class="brand-name">QUORVEL</span></div>
    </header>

    <p class="holder">Helen <strong>Trasko</strong> &nbsp;/ <span class="role">director</span></p>

    <div class="company-block">
      <p class="company-name">Quorvel Software Limited</p>
      <p class="company-address">42B Milbrook Lane, Epsom,<br>Surrey, KT19 4DN</p>
    </div>

    <dl class="contact-list">
      <dt>T.</dt><dd>+44 (0)1372 640913</dd>
      <dt>M.</dt><dd>+44 (0)7945 216804</dd>
      <dt>E.</dt><dd>htrasko@quorvel.net</dd>
      <dt>W.</dt><dd>www.quorvel.net</dd>
    </dl>

    <div class="foot-stripe"></div>
  </section>

</body>
</html>
```